Women's Online Clothing Boutique Needs Business Cards

I already have a logo that I would like to use. Some of the things that interest me is black business cards, foil embossed logo, glossy embossed logo, leopard print, no yellow font, rounded edges. I even like just a large logo on the front side with all of my information on the back side.

Contact Information for Business Card

https://silverheron.shopvenlo.com/
https://www.pagelink.net/thesilverheronboutique/
https://www.picfeed.net/thesilverheronboutique/
silverheronboutique@mailora.net

Requirements
Must have
• My Logo
Nice to have
• Leopard Print
Should not have
• No Yellow Font

```html
<!DOCTYPE html>
<html lang="en">
<head>
<meta charset="utf-8">
<title>The Silver Heron Boutique – Business Cards</title>
<link href="https://fonts.googleapis.com/css2?family=Nunito:wght@400&display=swap" rel="stylesheet">
<style>
  :root {
    --backdrop: #cbcbcb;
    --card-front: #141414;
    --card-back: #2a2a2b;
    --pattern-light: #4a4a4a;
    --pattern-dark: #1c1c1c;
    --gold: #c9a13c;
    --ink-light: #f1f1f1;
  }
  * { box-sizing: border-box; margin: 0; padding: 0; }
  html, body {
    width: 1200px; height: 800px; overflow: hidden;
    background: var(--backdrop);
    font-family: "Nunito", sans-serif;
  }
  .sheet {
    position: relative; width: 1200px; height: 800px;
  }
  .card {
    position: absolute; top: 257px;
    width: 500px; height: 286px;
    border-radius: 8px; overflow: hidden;
  }
  .card--front { left: 60px; background: var(--card-front); }
  .card--back { left: 640px; background: var(--card-back); }

  .leopard-print {
    position: absolute; inset: 0;
    background: linear-gradient(135deg, var(--pattern-light) 0%, #2c2c2c 35%, var(--pattern-dark) 70%, #101010 100%);
  }

  .wordmark {
    position: absolute; inset: 0;
    display: flex; flex-direction: column; align-items: center; justify-content: center;
    color: var(--gold); font-weight: 400; line-height: 1;
  }
  .wordmark__the { font-size: 13px; letter-spacing: 4px; margin-bottom: 6px; }
  .wordmark__name { font-size: 46px; }
  .wordmark__rule { width: 300px; height: 1px; background: var(--gold); margin: 10px 0; }
  .wordmark__sub { font-size: 26px; letter-spacing: 1px; }

  .contact-list {
    position: absolute; left: 150px; top: 62px;
    list-style: none; width: 300px;
  }
  .contact-item {
    display: flex; align-items: center; gap: 10px;
    padding: 8px 0 9px;
    border-bottom: 1px solid var(--gold);
    color: var(--ink-light); font-size: 13px;
  }
  .contact-item__mark {
    flex: none; width: 11px; height: 11px;
  }
</style>
</head>
<body>
<main class="sheet">
  <section class="card card--front" aria-label="Front of business card">
    <div class="leopard-print" role="img" aria-label="Glossy black leopard print pattern"></div>
    <div class="wordmark">
      <span class="wordmark__the">THE</span>
      <span class="wordmark__name">Silver Heron</span>
      <span class="wordmark__rule"></span>
      <span class="wordmark__sub">Boutique</span>
    </div>
  </section>

  <section class="card card--back" aria-label="Back of business card">
    <ul class="contact-list">
      <li class="contact-item">
        <svg class="contact-item__mark" viewBox="0 0 11 11" aria-hidden="true"><rect width="11" height="11" rx="2" fill="#c9a13c"/></svg>
        /thesilverheronboutique
      </li>
      <li class="contact-item">
        <svg class="contact-item__mark" viewBox="0 0 11 11" aria-hidden="true"><rect width="11" height="11" rx="2" fill="#c9a13c"/></svg>
        /thesilverheronboutique
      </li>
      <li class="contact-item">
        <svg class="contact-item__mark" viewBox="0 0 11 11" aria-hidden="true"><rect x="0.5" y="2" width="10" height="7" fill="none" stroke="#c9a13c"/><path d="M0.5 2 L5.5 6 L10.5 2" fill="none" stroke="#c9a13c"/></svg>
        silverheronboutique@mailora.net
      </li>
      <li class="contact-item">
        <svg class="contact-item__mark" viewBox="0 0 11 11" aria-hidden="true"><circle cx="5.5" cy="5.5" r="5" fill="none" stroke="#c9a13c"/><ellipse cx="5.5" cy="5.5" rx="2.2" ry="5" fill="none" stroke="#c9a13c"/><line x1="0.5" y1="5.5" x2="10.5" y2="5.5" stroke="#c9a13c"/></svg>
        silverheron.shopvenlo.com
      </li>
    </ul>
  </section>
</main>
</body>
</html>
```